Pet sitting and Dog Walking Postcard distributed to new home owners in our target market

We need a two-sided postcard (or rack card, size can be anything rack card size or smaller) that is going in a folder that will be distributed each month to new homeowners in our target area. I would like the design to be similar to our brochure which will be uploaded here for you to see. It needs much less information than the brochure.
Should include services we offer; and our 4 systems: online registration, complimentary consultation, flexible scheduling, visits with reports and photos. Should also include our contact information (website, email, phone). Photos from the brochure can be used. Tagline from the cover of the brochure can be used. Call to action should be: Register on our website today to receive a free consultation and $20 off your first booking (when requesting a service, mention the promo code: welcome20).

```html
<!DOCTYPE html>
<html lang="en">
<head>
<meta charset="utf-8">
<title>Tailside Pet Care – Rack Card</title>
<link rel="stylesheet" href="https://fonts.googleapis.com/css2?family=Open+Sans:ital,wght@0,400;0,600;0,700;0,800;1,400;1,600&display=swap">
<style>
  :root{
    --purple:#56415e;
    --purple-dark:#48354f;
    --green:#5cb946;
    --white:#ffffff;
    --ink:#4a3a52;
    --backdrop:#e8e6e3;
  }
  *{box-sizing:border-box;margin:0;padding:0}
  html,body{width:1200px;height:1104px;overflow:hidden}
  body{background:var(--backdrop);font-family:"Open Sans",Arial,sans-serif;position:relative}

  .card{position:absolute;top:107px;width:400px;height:890px;background:var(--white);overflow:hidden;box-shadow:0 6px 18px rgba(0,0,0,.18)}
  .card--front{left:170px}
  .card--back{left:630px}

  .panel{position:absolute;left:0;width:400px;background:var(--purple)}

  /* brand */
  .brand-mark{position:absolute;left:166px;top:26px;width:68px;height:68px;border-radius:50%;background:var(--purple)}
  .brand-name{position:absolute;left:0;top:106px;width:400px;text-align:center;color:var(--purple);font-weight:700;font-size:24px;letter-spacing:2px}

  .photo{position:absolute;left:0;width:400px}
  .photo--owner{top:160px;height:300px;background:linear-gradient(135deg,#f3efe9 0%,#e4d8c9 45%,#b8a089 70%,#6d5a4c 100%)}
  .photo--sofa{top:0;height:260px;background:linear-gradient(180deg,#d8cfc2 0%,#c9bfb2 30%,#8c8f9f 55%,#8a7a66 100%)}
  .photo--dog{left:312px;top:726px;width:84px;height:122px;border-radius:42px 42px 8px 8px;background:linear-gradient(180deg,#f4ede2 0%,#e6d7c0 100%)}

  .swoosh{position:absolute;left:0;width:400px}

  /* front copy */
  .headline{position:absolute;left:0;width:400px;text-align:center;font-weight:700;font-size:25px;line-height:32px}
  .headline__main{color:var(--white)}
  .headline__accent{color:var(--green)}

  .offer{position:absolute;left:18px;top:558px;width:364px;height:96px;border:1.5px dashed rgba(255,255,255,.75);border-radius:10px;text-align:center;color:var(--white)}
  .offer__line{font-size:16px;line-height:21px}
  .offer__line--first{margin-top:10px}
  .offer__accent{color:var(--green);font-weight:700;text-transform:uppercase}
  .offer__fine{font-size:8.5px;margin-top:3px}

  .services{position:absolute;top:684px;list-style:none;color:var(--white);font-size:12.5px;line-height:20px}
  .services--a{left:62px}
  .services--b{left:186px}
  .services li{position:relative;padding-left:17px;white-space:nowrap}
  .services li::before{content:"";position:absolute;left:0;top:5px;width:10px;height:10px;border-radius:50%;background:var(--green)}

  .service-area{position:absolute;left:0;top:756px;width:340px;text-align:center;color:var(--white);font-size:13px;line-height:18px}

  .phone-pill{position:absolute;left:70px;top:797px;width:204px;height:36px;border-radius:18px;background:var(--green);color:var(--white);font-weight:700;font-size:20px;display:flex;align-items:center;justify-content:center;gap:8px}

  .footer{position:absolute;left:0;top:850px;width:400px;height:40px;display:flex;align-items:center;justify-content:center;gap:8px;font-size:11px;color:var(--ink);font-weight:600}
  .footer__sep{width:1px;height:16px;background:var(--ink)}

  /* back copy */
  .badge{position:absolute;left:132px;top:166px;width:136px;height:136px;border-radius:50%;background:var(--white);border:3px solid var(--purple);display:flex;flex-direction:column;align-items:center;justify-content:center;color:var(--purple);font-weight:700;font-size:16px;letter-spacing:1.5px;line-height:22px}

  .intro{position:absolute;left:38px;top:346px;width:330px;color:var(--white);font-size:10px;line-height:13.5px}

  .system{position:absolute;left:40px;width:330px}
  .system__icon{position:absolute;left:0;top:2px;width:44px;height:44px;border-radius:50%;background:var(--white);display:flex;align-items:center;justify-content:center}
  .system__title{position:absolute;left:64px;top:0;color:var(--green);font-weight:700;font-size:12px}
  .system__text{position:absolute;left:64px;top:18px;width:250px;color:var(--white);font-style:italic;font-size:10px;line-height:13px}
  .system__text--narrow{width:200px}
</style>
</head>
<body>

<!-- Front side -->
<section class="card card--front">
  <div class="brand-mark"></div>
  <div class="brand-name">TAILSIDE PET CARE</div>

  <div class="photo photo--owner" role="img" aria-label="Photo of a smiling woman on a sofa hugging her dog in a bright living room"></div>

  <div class="panel" style="top:450px;height:400px"></div>
  <svg class="swoosh" style="top:390px" width="400" height="70" viewBox="0 0 400 70">
    <path d="M0 18 Q190 78 400 4 L400 70 L0 70Z" fill="var(--green)"/>
    <path d="M0 34 Q200 84 400 18 L400 70 L0 70Z" fill="var(--purple)"/>
  </svg>

  <h1 class="headline" style="top:480px">
    <span class="headline__main">Prioritize Yourself.</span><br>
    <span class="headline__accent">We'll Focus on Your Pets.</span>
  </h1>

  <div class="offer">
    <p class="offer__line offer__line--first">Register on our website today</p>
    <p class="offer__line offer__accent">To receive a free consultation</p>
    <p class="offer__line">and <strong>$20 off</strong> your first booking</p>
    <p class="offer__fine">(when requesting a service, mention the promo code: welcome20).</p>
  </div>

  <ul class="services services--a">
    <li>Dog Walking</li>
    <li>Pet Sitting</li>
    <li>Cat Sitting</li>
  </ul>
  <ul class="services services--b">
    <li>Small Animal Care</li>
    <li>Overnights</li>
    <li>Boarding</li>
  </ul>

  <p class="service-area">Proudly serving Elmbrook &amp; surrounding<br>neighborhoods for over 15 years.</p>

  <svg class="swoosh" style="top:818px" width="400" height="40" viewBox="0 0 400 40">
    <path d="M0 34 Q220 40 400 6 L400 40 L0 40Z" fill="var(--green)"/>
    <path d="M0 40 Q220 44 400 16 L400 40Z" fill="var(--white)"/>
  </svg>

  <div class="phone-pill">
    <svg width="22" height="22" viewBox="0 0 24 24"><circle cx="12" cy="12" r="10.5" fill="none" stroke="var(--white)" stroke-width="2"/><path d="M8.6 7.2l1.6-.4 1 2.4-1 .9a6 6 0 0 0 2.7 2.7l.9-1 2.4 1-.4 1.6c-3.9.2-7.4-3.3-7.2-7.2z" fill="var(--white)"/></svg>
    555-014-WOOF
  </div>

  <div class="photo photo--dog" role="img" aria-label="Photo of a white Labrador puppy lying down"></div>

  <footer class="footer">
    <span>hello@tailsidepets.com</span><span class="footer__sep"></span><span>www.tailsidepets.com</span>
  </footer>
</section>

<!-- Back side -->
<section class="card card--back">
  <div class="photo photo--sofa" role="img" aria-label="Overhead photo of a woman relaxing on a grey sofa with her dog and cushions"></div>

  <div class="panel" style="top:250px;height:600px"></div>
  <svg class="swoosh" style="top:196px" width="400" height="80" viewBox="0 0 400 80">
    <path d="M0 14 Q200 70 400 8 L400 80 L0 80Z" fill="var(--white)"/>
    <path d="M0 26 Q200 82 400 20 L400 80 L0 80Z" fill="var(--green)"/>
    <path d="M0 38 Q200 92 400 32 L400 80 L0 80Z" fill="var(--purple)"/>
  </svg>

  <div class="badge"><span>TAILSIDE</span><span>PET CARE</span></div>

  <h2 class="headline" style="top:308px;font-size:22px">
    <span class="headline__main">Ready To Free Up </span><span class="headline__accent">Your Time?</span>
  </h2>

  <p class="intro">We are here to uncomplicate your life! Our systems and processes allow for seamless scheduling, service and billing. Give us a few minutes of your time and we will deliver it back to you tenfold!</p>

  <div class="system" style="top:430px">
    <div class="system__icon"><svg width="24" height="24" viewBox="0 0 24 24"><rect x="3" y="5" width="18" height="12" rx="1.5" fill="none" stroke="var(--purple)" stroke-width="2"/><rect x="1" y="18" width="22" height="2" rx="1" fill="var(--purple)"/></svg></div>
    <h3 class="system__title">Online Registration</h3>
    <p class="system__text">Click on the register link on our homepage to begin online registration or submit a request form if you would like more information first.</p>
  </div>

  <div class="system" style="top:517px">
    <div class="system__icon"><svg width="24" height="24" viewBox="0 0 24 24"><path d="M4 5h16v10H10l-4 4v-4H4z" fill="var(--purple)"/><circle cx="9" cy="10" r="1.2" fill="var(--white)"/><circle cx="12" cy="10" r="1.2" fill="var(--white)"/><circle cx="15" cy="10" r="1.2" fill="var(--white)"/></svg></div>
    <h3 class="system__title">Complimentary Consultation</h3>
    <p class="system__text">Request a consultation through our online portal. We'll reach out to you if you get stuck! Then we'll coordinate a meeting at your convenience.</p>
  </div>

  <div class="system" style="top:606px">
    <div class="system__icon"><svg width="24" height="24" viewBox="0 0 24 24"><rect x="3" y="5" width="18" height="16" rx="1.5" fill="none" stroke="var(--purple)" stroke-width="2"/><rect x="3" y="5" width="18" height="4" fill="var(--purple)"/><path d="M7 12h2M11 12h2M15 12h2M7 16h2M11 16h2M15 16h2" stroke="var(--purple)" stroke-width="2"/></svg></div>
    <h3 class="system__title">Flexible Scheduling</h3>
    <p class="system__text">Once we've met, we will be able to custom schedule your visits to fit your needs. You can always adjust your schedule through our portal app if your needs change.</p>
  </div>

  <div class="system" style="top:700px">
    <div class="system__icon"><svg width="24" height="24" viewBox="0 0 24 24"><path d="M3 8h4l2-3h6l2 3h4v11H3z" fill="var(--purple)"/><circle cx="12" cy="13" r="3.5" fill="var(--white)"/></svg></div>
    <h3 class="system__title">Visits with Reports and Photos</h3>
    <p class="system__text system__text--narrow">Your pets will be cared for by our elite team of Pet Care Specialists. After each visit, you will receive an emailed report with photo.</p>
  </div>

  <svg class="swoosh" style="top:818px" width="400" height="40" viewBox="0 0 400 40">
    <path d="M0 34 Q220 40 400 6 L400 40 L0 40Z" fill="var(--green)"/>
    <path d="M0 40 Q220 44 400 16 L400 40Z" fill="var(--white)"/>
  </svg>

  <div class="phone-pill">
    <svg width="22" height="22" viewBox="0 0 24 24"><circle cx="12" cy="12" r="10.5" fill="none" stroke="var(--white)" stroke-width="2"/><path d="M8.6 7.2l1.6-.4 1 2.4-1 .9a6 6 0 0 0 2.7 2.7l.9-1 2.4 1-.4 1.6c-3.9.2-7.4-3.3-7.2-7.2z" fill="var(--white)"/></svg>
    555-014-WOOF
  </div>

  <div class="photo photo--dog" role="img" aria-label="Photo of a white Labrador puppy lying down"></div>

  <footer class="footer">
    <span>hello@tailsidepets.com</span><span class="footer__sep"></span><span>www.tailsidepets.com</span>
  </footer>
</section>

</body>
</html>
```